A portal to our hosted desktop

Looking for a web portal into our hosted desktop. It will be accessible via http://www.korvelnet.com.au/pages/portal which is not created yet.

We are happy for the designs to link in with the current website design but also happy to accept designs that do not. We would like the website to have the following buttons:

• Login
• Speed Test
• Log Support Request
• Resources

We would like a system notification area that we can display messages on.

We also like the idea of a traffic light system (Green, Orange, Red). Green, meaning all systems are a go. Orange meaning maintenance is occurring and red meaning the system is down.

Target Market(s)

Web Developers and Graphic Designers

Coding

Coded - Design and coding required

Number of Pages Required

1 page

Requirements
Must have
• Buttons for the following:
• Login
• Speed Test
• Log Support Request
• Resources
• Notification area and color system to know if everything is a-o-k

```html
<!DOCTYPE html>
<html lang="en">
<head>
<meta charset="utf-8">
<title>KORVELNET Hosted Desktop Login Portal</title>
<link rel="stylesheet" href="https://fonts.googleapis.com/css2?family=Raleway:wght@400;500;600&family=Open+Sans:wght@400&display=swap">
<style>
:root{
  --brand-blue:#2a8ad8;
  --navy:#173a55;
  --navy-dark:#0f2d45;
  --text-dark:#333;
  --hero-deep:#2f7fcf;
  --hero-light:#5db8e2;
  --green:#5fc70f;
  --orange:#ff7d0a;
  --red:#d9000f;
  --white:#fff;
}
*{margin:0;padding:0;box-sizing:border-box}
html,body{width:1200px;height:1051px;overflow:hidden;background:var(--white)}
body{font-family:'Raleway',sans-serif;color:var(--text-dark);position:relative}
a{text-decoration:none;color:inherit}

.site-header{height:90px;position:relative}
.brand{position:absolute;left:184px;top:10px;display:flex;align-items:center;gap:8px}
.brand-mark{width:62px;height:62px;border-radius:50%;background:var(--brand-blue)}
.brand-text{display:flex;flex-direction:column}
.brand-name{font-family:'Raleway',sans-serif;font-weight:600;font-size:32px;color:var(--brand-blue);line-height:1}
.brand-tag{font-size:9px;letter-spacing:2px;color:var(--brand-blue);margin-top:3px}
.main-nav{position:absolute;right:199px;top:38px;display:flex;gap:27px;font-size:14.5px;color:#333}

.hero{position:absolute;top:90px;left:0;width:1200px;height:510px;
  background:radial-gradient(ellipse at 65% 45%,var(--hero-light) 0%,#4aa7dc 45%,var(--hero-deep) 100%)}
.portal-panel{position:absolute;left:318px;top:144px;width:564px;height:189px;border-radius:8px;
  background:rgba(220,235,242,.78);text-align:center}
.portal-title{font-weight:500;font-size:31px;line-height:33px;margin-top:24px;text-transform:uppercase}
.portal-title .accent{color:var(--brand-blue);display:block}
.portal-title .dark{color:var(--navy-dark);display:block}
.btn-login{position:absolute;left:211px;top:101px;width:152px;height:34px;border:1px solid #fff;
  background:linear-gradient(#4aa3e8,#1e78cc);color:#fff;font-size:15px;font-weight:500;
  display:flex;align-items:center;justify-content:center;gap:6px}
.btn-row{position:absolute;top:144px;left:98px;display:flex;gap:9px}
.btn-secondary{height:32px;background:linear-gradient(#1f4766,#0e2b42);color:#fff;font-size:13px;font-weight:500;
  display:flex;align-items:center;justify-content:center}

.notification{position:absolute;left:196px;top:675px;width:500px}
.notification h2{font-weight:400;font-size:31px;color:var(--brand-blue);margin-bottom:14px}
.notification p{font-family:'Open Sans',sans-serif;font-size:11px;line-height:18px;color:#444;margin-bottom:4px;padding-left:2px}

.status-list{position:absolute;left:738px;top:658px;display:flex;flex-direction:column;gap:9px}
.status{width:260px;height:55px;border-radius:28px;display:flex;align-items:center;color:#fff;font-size:16.5px;padding-left:4px}
.status-icon{width:48px;height:48px;border-radius:50%;border:2px solid #fff;display:flex;align-items:center;justify-content:center;margin-right:15px}
.status-available{background:var(--green)}
.status-maintenance{background:var(--orange)}
.status-down{background:var(--red);margin-left:3px}

.site-footer{position:absolute;top:950px;left:0;width:1200px;height:101px;background:var(--navy)}
.footer-nav{position:absolute;left:183px;top:28px;display:flex;gap:24px;font-size:14.5px;color:#dfe8ef}
.copyright{position:absolute;left:183px;top:56px;font-family:'Open Sans',sans-serif;font-size:10px;color:#a9bccb}
.social{position:absolute;right:199px;top:28px;display:flex;gap:10px}
.social span{width:18px;height:18px;background:#fff;border-radius:3px}
</style>
</head>
<body>
<header class="site-header">
  <a class="brand" href="#">
    <span class="brand-mark"></span>
    <span class="brand-text">
      <span class="brand-name">KORVELNET</span>
      <span class="brand-tag">FAST, STABLE, SECURE</span>
    </span>
  </a>
  <nav class="main-nav">
    <a href="#">Home</a><a href="#">Login</a><a href="#">Speed Test</a><a href="#">Log Support Request</a><a href="#">Resources</a>
  </nav>
</header>

<section class="hero" role="img" aria-label="Textured blue wall background">
  <div class="portal-panel">
    <h1 class="portal-title"><span class="accent">KORVELNET Hosted Desktop</span><span class="dark">Login Portal</span></h1>
    <a class="btn-login" href="http://www.korvelnet.com.au/pages/portal">LOGIN
      <svg width="10" height="12" viewBox="0 0 10 12"><path d="M2 1l5 5-5 5" fill="none" stroke="#fff" stroke-width="2.4"/></svg></a>
    <div class="btn-row">
      <a class="btn-secondary" style="width:106px;font-size:14px" href="#">Speed Test</a>
      <a class="btn-secondary" style="width:149px" href="#">Log Support Request</a>
      <a class="btn-secondary" style="width:106px;font-size:14px" href="#">Resources</a>
    </div>
  </div>
</section>

<section class="notification">
  <h2>System Notification</h2>
  <p>Curabitur iaculis tempus eros Curabitur vel mi sit amet magna malesuada ultrices Ut nisi erat fermentum vel congue id euismod in elit Fusce ultricies</p>
  <p>Arci ac feugiat suscipit leo massa sodales velit et scelerisque mi tortor at ipsum cligula augue bibendum accumsan vestibulum ut commodo a mi Morbi ornare gravida elit Integer congue augue et malesuada iaculis ipsum dui aliquet felis at cursus magna nisl nec elit</p>
</section>

<section class="status-list">
  <div class="status status-available">
    <span class="status-icon"><svg width="22" height="20" viewBox="0 0 22 20"><rect x="1" y="1" width="20" height="13" rx="1" fill="none" stroke="#fff" stroke-width="2"/><rect x="3" y="3" width="16" height="9" fill="#fff"/><rect x="9" y="14" width="4" height="3" fill="#fff"/><rect x="6" y="17" width="10" height="2" fill="#fff"/></svg></span>
    System Available
  </div>
  <div class="status status-maintenance">
    <span class="status-icon"><svg width="24" height="24" viewBox="0 0 24 24"><path d="M3 21l10-10" stroke="#fff" stroke-width="3.5" stroke-linecap="round"/><circle cx="16" cy="8" r="5.5" fill="#fff"/><path d="M16 4l4 4" stroke="var(--orange)" stroke-width="3"/></svg></span>
    Maintenance Occurring
  </div>
  <div class="status status-down">
    <span class="status-icon"><svg width="24" height="24" viewBox="0 0 24 24"><path d="M19 5c-6 0-9 3-9 9" fill="none" stroke="#fff" stroke-width="3.5"/><path d="M4 13h12l-6 8z" fill="#fff"/></svg></span>
    System Down
  </div>
</section>

<footer class="site-footer">
  <nav class="footer-nav">
    <a href="#">Home</a><a href="#">Login</a><a href="#">Speed Test</a><a href="#">Log Support Request</a><a href="#">Resources</a>
  </nav>
  <p class="copyright">All right reserved &nbsp;©&nbsp; 2015 KORVELNET PTY LTD</p>
  <div class="social"><span></span><span></span></div>
</footer>
</body>
</html>
```